KIVO 248
I need double sided standard sized Business Card [3.5" x 2"]
Open to designers choice
Modern
Pavel Rudakovsky
PO BOX 7132
Marlow, OR 90318
pavel@tumq4.com
kivo248.com

```html
<!DOCTYPE html>
<html lang="en">
<head>
<meta charset="utf-8">
<title>KIVO 248 — Business Card</title>
<link rel="stylesheet" href="https://fonts.googleapis.com/css2?family=Exo+2:wght@300;400;600&display=swap">
<style>
  :root {
    --backdrop: #e9e6e2;
    --card: #ffffff;
    --accent-red: #e2321d;
    --accent-orange: #f26a21;
    --corner-grey: #4a4a4a;
    --text-grey: #6b6b6b;
    --name-red: #d8321f;
  }
  * { margin: 0; padding: 0; box-sizing: border-box; }
  html, body {
    width: 1200px; height: 914px; overflow: hidden;
    background: var(--backdrop);
    font-family: "Exo 2", sans-serif;
  }
  .business-card {
    position: absolute; left: 100px; top: 171px;
    width: 1000px; height: 571px;
    background: var(--card);
    box-shadow: 0 10px 30px rgba(0,0,0,0.18);
    overflow: hidden;
  }
  .corner-accent {
    position: absolute; right: 0; top: 0;
    width: 420px; height: 360px;
    background: linear-gradient(to bottom left,
      var(--accent-red) 0%,
      var(--accent-orange) 30%,
      rgba(242,106,33,0.35) 55%,
      rgba(255,255,255,0) 75%);
  }
  .brand {
    position: absolute; left: 80px; top: 64px;
    display: flex; align-items: center; gap: 22px;
  }
  .brand-square {
    width: 110px; height: 110px; border-radius: 18px;
    background: var(--accent-orange);
  }
  .brand-name {
    font-weight: 400; font-size: 70px; letter-spacing: 2px;
    color: var(--accent-orange);
  }
  .contact-list {
    position: absolute; left: 84px; top: 222px;
    list-style: none;
  }
  .contact-item {
    display: flex; align-items: center; gap: 12px;
    height: 27px;
    font-size: 17px; font-weight: 400; letter-spacing: 2.5px;
    color: var(--text-grey); text-transform: uppercase;
  }
  .contact-item.indented { padding-left: 32px; }
  .contact-item.lowercase { text-transform: none; }
  .contact-icon { width: 20px; height: 20px; flex: none; }
  .signature {
    position: absolute; right: 60px; bottom: 48px;
    text-align: right; letter-spacing: 2.5px;
  }
  .signature-name { font-size: 20px; color: var(--name-red); }
  .signature-role { font-size: 18px; color: var(--text-grey); }
</style>
</head>
<body>
  <article class="business-card">
    <div class="corner-accent" role="img" aria-label="Orange-red and grey decorative corner graphic"></div>

    <header class="brand">
      <span class="brand-square"></span>
      <span class="brand-name">KIVO 248</span>
    </header>

    <ul class="contact-list">
      <li class="contact-item">
        <svg class="contact-icon" viewBox="0 0 20 20"><circle cx="10" cy="10" r="10" fill="var(--accent-red)"/><path d="M10 4a4 4 0 0 0-4 4c0 3 4 8 4 8s4-5 4-8a4 4 0 0 0-4-4z" fill="#fff"/></svg>
        PO BOX 7132
      </li>
      <li class="contact-item indented">Marlow, OR 90318</li>
      <li class="contact-item">
        <svg class="contact-icon" viewBox="0 0 20 20"><circle cx="10" cy="10" r="10" fill="var(--accent-red)"/><rect x="7" y="4" width="6" height="12" rx="1.5" fill="#fff"/></svg>
        5550142736
      </li>
      <li class="contact-item">
        <svg class="contact-icon" viewBox="0 0 20 20"><circle cx="10" cy="10" r="10" fill="var(--accent-red)"/><path d="M6 5l2 0 1 3-1.5 1a7 7 0 0 0 3.5 3.5l1-1.5 3 1 0 2c-5 0-9-4-9-9z" fill="#fff"/></svg>
        5550179384
      </li>
      <li class="contact-item">
        <svg class="contact-icon" viewBox="0 0 20 20"><circle cx="10" cy="10" r="10" fill="var(--accent-red)"/><rect x="5" y="6" width="10" height="8" fill="#fff"/></svg>
        5550142736
      </li>
      <li class="contact-item lowercase">
        <svg class="contact-icon" viewBox="0 0 20 20"><circle cx="10" cy="10" r="10" fill="var(--accent-red)"/><rect x="5" y="6" width="10" height="8" fill="#fff"/><path d="M5 6l5 4 5-4" stroke="var(--accent-red)" stroke-width="1.2" fill="none"/></svg>
        pavel@tumq4.com
      </li>
      <li class="contact-item lowercase indented">www.kivo248.com</li>
    </ul>

    <footer class="signature">
      <p class="signature-name">Pavel Rudakovsky</p>
      <p class="signature-role">CEO</p>
    </footer>
  </article>
</body>
</html>
```